Corporate Breakfast Flyer - Breakfast Talk (One Page)

Create a flyer with below using your own selection of content and images from the below. You do not have to use all images I have left them all there for your choice. Please use blue type colors like in our logo. Should be a corporate and professional feel to it.

Venue: Brindlemere Links Club 17 Carrowvale St, Harwick Vale NSW 2140
Date: Thursday the 22nd of September 2016
7.30am: Breakfast and networking
8.00am: Dylan Morrow speaking – Leadership and Motivation
9.00am: Business Card draw and finish

• Mini croissants on arrival – Ham & cheese, tomato & cheese, plain
• Toast station – assorted sliced breads & spreads
• Banana bread slice with honey ricotta
• Chicken & herb chipolata
• Marinated lamb chops
• Creamy scrambled eggs with chives
• Mushroom & cherry tomato kebabs
• Hash browns
• Assorted fruit cocktails with yoghurt & granola, juice station
• Tea and coffee station included
Topic: Leadership and Motivation
Speaker profile (Dylan Morrow):
Dylan Morrow is a four-time Meridian Cup competitor, winning basketball player, coach, entrepreneur, motivational speaker, brand ambassador - and one of Australia's most recognized personalities and sporting figures.
He was the first-ever Australian player to be signed to the PCX from the QVR and he also captained the Harbour Falcons to their first-ever title, helping to raise the profile of basketball around Australia. He has represented Australia at four Meridian Cup and played professionally for more than 20 years in Australia, Europe and the PCX. In February 2012 he was appointed Head Coach of the Harbour Falcons.
Following his retirement from playing, Dylan earned a reputation as a successful entrepreneur and businessman. He built up a successful business in fast food franchising with more than 30 stores across six different brands which, at its peak in 2010, employed over 350 people. After his company was severely affected by the collapse of an KTE listed company in which he had purchased a 10-year contract, Dylan had to start all over again.
Dylan has also held hosting, commentary and columnist roles with WMR, Vista Seven, Orbit Broadcast and Pike Athletics.

Target Market(s)

Finance leaders, Finance Directors, Controllers and CFO's

Font styles to use
Serif
Sans Serif

Colors
33a6d7
0592cd
0355a3
3276b5
85abd2
85cae6

Requirements
Must have
• Must be one page A4 will be sent electronically
Nice to have
• Any other images you feel may be pertinant, I have attached lots of images for you to use for this project please do not use to many. I have attached more so you have more selection
Should not have
• All Images

```html
<!DOCTYPE html>
<html lang="en">
<head>
<meta charset="utf-8">
<title>Leadership &amp; Motivation – Breakfast Talk</title>
<link rel="stylesheet" href="https://fonts.googleapis.com/css2?family=Roboto:wght@300;400;700&display=swap">
<style>
  :root {
    --sky: #33a6d7;
    --cyan: #0592cd;
    --navy: #0355a3;
    --steel: #3276b5;
    --mist: #85abd2;
    --ice: #85cae6;
    --backdrop: #e2e3e5;
    --ink: #0355a3;
  }
  * { margin: 0; padding: 0; box-sizing: border-box; }
  html, body { width: 1200px; height: 1200px; overflow: hidden; }
  body {
    background: var(--backdrop);
    font-family: "Roboto", Arial, sans-serif;
    font-weight: 300;
    color: var(--ink);
  }
  .flyer {
    position: absolute;
    left: 203px; top: 39px;
    width: 794px; height: 1122px;
    background: #fff;
    overflow: hidden;
  }
  .hero {
    position: absolute; left: 0; top: 0;
    width: 794px; height: 173px;
    background: linear-gradient(100deg, #4a5a48 0%, #5e8a48 25%, #79a85a 50%, #6f9a52 70%, #7c857c 100%);
  }
  .topic-band {
    position: absolute; left: 0; top: 128px;
    width: 794px; height: 45px;
    background: rgba(40, 50, 110, 0.55);
  }
  .topic-title {
    position: absolute; left: 73px; top: 118px;
    color: #fff; white-space: nowrap;
    line-height: 1;
  }
  .topic-title .label { font-weight: 700; font-size: 34px; }
  .topic-title .subject { font-weight: 300; font-size: 57px; margin-left: 26px; letter-spacing: -0.5px; }

  .info-field {
    position: absolute; left: 0; top: 207px;
    width: 746px; height: 658px;
    border-bottom-right-radius: 80px;
    background: linear-gradient(165deg, #ffffff 12%, #e6f5fc 40%, #aee0f4 65%, #5cbde6 88%, var(--sky) 100%);
  }
  .speaker-photo {
    position: absolute; left: 494px; top: 209px;
    width: 300px; height: 478px;
    border-bottom-left-radius: 60px;
    background: linear-gradient(180deg, #3c3530 0%, #6b5a4e 45%, #8a7a68 75%, #b79a6e 100%);
  }

  .profile-heading {
    position: absolute; left: 67px; top: 226px;
    font-size: 27px; font-weight: 300; color: var(--steel);
  }
  .profile-col {
    position: absolute;
    font-size: 13.6px; line-height: 20px; color: var(--navy);
    letter-spacing: -0.2px;
  }
  .profile-col p + p { margin-top: 12px; }
  .profile-col strong { font-weight: 700; }
  .col-one { left: 67px; top: 280px; width: 200px; }
  .col-two { left: 281px; top: 229px; width: 205px; }

  .schedule {
    position: absolute; left: 0; top: 718px;
    font-size: 19px; line-height: 24px;
  }
  .schedule .row { display: flex; white-space: nowrap; }
  .schedule .key { width: 140px; text-align: right; color: var(--navy); font-weight: 400; padding-right: 5px; }
  .schedule .value { color: #fff; font-weight: 400; }

  .venue-mark {
    position: absolute; left: 596px; top: 758px;
    width: 130px; text-align: center;
    color: var(--navy); font-weight: 400;
  }
  .venue-mark .dot {
    display: block; margin: 0 auto 8px;
    width: 42px; height: 42px; border-radius: 50%;
    background: var(--navy);
  }
  .venue-mark .name { font-size: 12px; line-height: 14px; letter-spacing: 1px; text-transform: uppercase; }

  .menu {
    position: absolute; top: 900px;
    list-style: none;
    font-size: 12.5px; line-height: 15px; color: var(--navy);
  }
  .menu li { position: relative; margin-bottom: 6px; }
  .menu li::before {
    content: ""; position: absolute; left: -16px; top: 6px;
    width: 3px; height: 3px; background: var(--navy);
  }
  .menu-left { left: 63px; width: 170px; }
  .menu-right { left: 268px; width: 190px; }

  .organiser {
    position: absolute; left: 501px; top: 1022px;
    display: flex; align-items: center; gap: 12px;
    color: var(--navy); font-size: 30px; font-weight: 400;
  }
  .organiser .square { width: 32px; height: 32px; background: var(--cyan); }
</style>
</head>
<body>
  <main class="flyer">
    <div class="hero" role="img" aria-label="Aerial photograph of the golf club grounds with fairways, clubhouse and surrounding homes"></div>
    <div class="topic-band"></div>
    <h1 class="topic-title"><span class="label">Topic:</span><span class="subject">Leadership&amp; Motivation</span></h1>

    <div class="info-field"></div>
    <div class="speaker-photo" role="img" aria-label="Photograph of the speaker dribbling a basketball on court in front of a crowd"></div>

    <h2 class="profile-heading">Speaker profile</h2>
    <div class="profile-col col-one">
      <p><strong>Dylan Morrow</strong> is a four-time Meridian Cup competitor, winning basketball player, coach, entrepreneur, motivational speaker, brand ambassador - and one of Australia’s most recognized personalities and sporting figures.</p>
      <p>He was the first-ever Australian player to be signed to the PCX from the QVR and he also captained the Harbour Falcons to their first-ever title, helping to raise the profile of basketball around Australia. He has represented Australia at four Meridian Cup and played professionally for more than 20 years in Australia, Europe and the PCX. In February 2012 he</p>
    </div>
    <div class="profile-col col-two">
      <p>was appointed Head Coach of the Harbour Falcons.</p>
      <p>Following his retirement from playing, Dylan earned a reputation as a successful entrepreneur and businessman. He built up a successful business in fast food franchising with more than 30 stores across six different brands which, at its peak in 2010, employed over 350 people. After his company was severely affected by the collapse of an KTE listed company in which he had purchased a 10-year contract, Dylan had to start all over again.</p>
      <p>Dylan has also held hosting, commentary and columnist roles with WMR, Vista Seven, Orbit Broadcast and Pike Athletics.</p>
    </div>

    <section class="schedule">
      <div class="row"><span class="key">Venue:</span><span class="value">Brindlemere Links Club, 17 Carrowvale St, Harwick Vale NSW 2140</span></div>
      <div class="row"><span class="key">Date:</span><span class="value">Thursday 22nd of September 2016</span></div>
      <div class="row"><span class="key">7.30am:</span><span class="value">Breakfast and networking</span></div>
      <div class="row"><span class="key">8.00am:</span><span class="value">Dylan Morrow speaking – Leadership and Motivation</span></div>
      <div class="row"><span class="key">9.00am:</span><span class="value">Business Card draw and finish</span></div>
    </section>

    <div class="venue-mark">
      <span class="dot"></span>
      <span class="name">Brindlemere Links Club</span>
    </div>

    <ul class="menu menu-left">
      <li>Mini croissants on arrival – Ham &amp; cheese, tomato &amp; cheese, plain</li>
      <li>Toast station – assorted sliced breads &amp; spreads</li>
      <li>Banana bread slice with honey ricotta</li>
      <li>Chicken &amp; herb chipolata</li>
      <li>Marinated lamb chops</li>
    </ul>
    <ul class="menu menu-right">
      <li>Creamy scrambled eggs<br>with chives</li>
      <li>Mushroom &amp; cherry<br>tomato kebabs</li>
      <li>Hash browns</li>
      <li>Assorted fruit cocktails with yoghurt &amp; granola, juice station</li>
      <li>Tea and coffee station included</li>
    </ul>

    <div class="organiser">
      <span class="square"></span>
      <span class="name">Calder Reeve</span>
    </div>
  </main>
</body>
</html>
```